Website Voskamp detective agency

Hi all,
After my last posted job for a logo (see attached file) I now need a website for my detective agency (Recherchebureau in Dutch)
I already have the better logo then my competitors thanks to you and your colleges working with Brandforge.
Please google the word recherchebureau to see what the competition has.
I will leave it up to you.
Bare in mind I take jobs from companies (staff steeling data or products) and private people (divorce matters etc.) so it should look very professional, trustworthy and different from the others.
My company uses creativity and new/ different ways to find the truth.
I think the logo already reflects this.
Of course I need it sliced for the website builder but if you can built it too please let me know. Then I would need a template were I can upload text and photo's etc.
Target Market(s)
Corporations
Small business
Privat people
Industry/Entity Type
Detective
Coding
Coded - Design and coding required
Number of Pages Required
5+ page
Requirements
Must have
- Responsive!
- Also this logo:
- http://www.kvbwacht.nl/wp-content/uploads/2014/05/keurmerk.png
- With the line:
- Erkend door het college van toezicht en certificering
- (This means recognized by the board of oversight)
Nice to have
- Here some extra.
- It is about website trend which I think is true.
- Please use google translate because it is in Dutch.
- http://www.lumenpost.com/archive/2014/11/17/10-webdesigntrends-voor-2015/

```html
<!DOCTYPE html>
<html lang="en">
<head>
<meta charset="utf-8">
<title>Voskamp Detective Agency</title>
<link rel="stylesheet" href="https://fonts.googleapis.com/css2?family=Open+Sans:wght@400;600;700;800&display=swap">
<style>
:root{
  --wine:#5b1c1e;
  --wine-dark:#461517;
  --wine-deep:#3a1011;
  --ink:#2b2b2b;
  --text:#6d6d6d;
  --line:#d9d9d9;
  --paper:#ffffff;
  --footer:#3b3b3b;
  --footer-bar:#2a2a2a;
  --footer-text:#b5b5b5;
}
*{box-sizing:border-box;margin:0;padding:0}
html,body{width:1200px;height:2200px;overflow:hidden;background:var(--paper)}
body{font-family:"Open Sans",Arial,sans-serif;color:var(--text)}
.page{position:relative;width:1200px;height:2200px;overflow:hidden}

/* hero */
.hero{position:absolute;left:0;top:0;width:1200px;height:512px;
  background:linear-gradient(100deg,#1d2630 0%,#2f3b47 40%,#4b5661 62%,#232b33 100%)}
.hero-shade{position:absolute;inset:0;background:linear-gradient(180deg,rgba(0,0,0,.35),rgba(0,0,0,.15) 50%,rgba(0,0,0,.45))}
.brand{position:absolute;left:100px;top:26px;display:flex;align-items:center;gap:10px;
  font-weight:700;font-size:16px;letter-spacing:2px;color:#fff}
.brand-mark{width:22px;height:22px;background:#fff}
.hero-title{position:absolute;left:100px;top:226px;color:#fff;font-weight:800;font-size:46px;line-height:56px;letter-spacing:3px}
.hero-tag{position:absolute;left:100px;top:352px;color:#fff;font-weight:400;font-size:26px;letter-spacing:11px}

/* nav */
.nav{position:absolute;left:0;top:512px;width:1200px;height:48px;background:var(--wine);
  display:flex;justify-content:center;padding:0 100px}
.nav a{flex:1;display:flex;align-items:center;justify-content:center;color:#f1e3e3;
  font-size:11px;font-weight:600;letter-spacing:.5px;text-decoration:none;text-transform:uppercase}
.nav a.is-active{background:#7a2a2c}
.nav .caret{margin-left:6px;font-size:8px}

/* welcome */
.welcome{position:absolute;left:150px;top:612px;width:900px;text-align:center}
.section-title{font-weight:700;font-size:26px;color:var(--ink);letter-spacing:.5px;text-transform:uppercase}
.welcome p{margin-top:18px;font-size:12px;line-height:20px}
.rule{position:absolute;left:100px;top:770px;width:1000px;height:1px;background:var(--line)}

/* services */
.services-title{position:absolute;left:0;top:790px;width:1200px;text-align:center;font-size:20px}
.services{position:absolute;left:100px;top:850px;width:1000px;display:flex;gap:40px}
.service{flex:1;display:flex;gap:16px}
.service-letter{flex:none;width:62px;height:62px;background:var(--wine-dark);color:#fff;
  font-weight:700;font-size:34px;display:flex;align-items:center;justify-content:center}
.service h3{font-size:15px;font-weight:700;color:var(--wine);text-transform:uppercase;margin-top:2px}
.service p{font-size:11px;line-height:17px;margin-top:6px}

/* attorneys */
.attorneys{position:absolute;left:0;top:995px;width:1200px;height:405px;
  background:linear-gradient(180deg,var(--wine-dark),var(--wine-deep))}
.attorneys .section-title{position:absolute;left:0;top:30px;width:1200px;text-align:center;color:#fff;font-size:22px}
.team{position:absolute;left:108px;top:82px;width:984px;display:flex;gap:20px}
.member{flex:1}
.member-photo{height:150px;border:3px solid #fff;background:linear-gradient(135deg,#d8d8d8,#8d8d8d)}
.member h4{margin-top:14px;font-size:12px;font-weight:700;color:#fff;text-transform:uppercase}
.member p{margin-top:8px;font-size:10px;line-height:15px;color:#d8c6c6}
.member hr{margin-top:14px;border:0;border-top:1px solid rgba(255,255,255,.25)}

/* events */
.events .section-title{position:absolute;left:0;top:1436px;width:1200px;text-align:center;font-size:22px}
.event-list{position:absolute;left:108px;top:1500px;width:992px;display:flex;gap:44px}
.event{flex:1;height:240px;border:1px solid var(--line);padding:8px;text-align:center;background:#fff}
.event-photo{height:118px;background:linear-gradient(135deg,#5a6570,#1f262d)}
.event h4{margin-top:12px;font-size:12px;font-weight:700;color:var(--ink);text-transform:uppercase}
.event p{margin-top:8px;font-size:10px;line-height:15px}
.event .more{display:inline-block;margin-top:8px;font-size:10px;font-weight:700;color:var(--ink)}

/* footer */
.footer{position:absolute;left:0;top:1760px;width:1200px;height:400px;background:var(--footer);color:var(--footer-text)}
.footer-brand{position:absolute;left:100px;top:210px;display:flex;align-items:center;gap:12px;
  color:#5a5a5a;font-weight:700;font-size:22px;letter-spacing:3px}
.footer-brand span.mark{width:34px;height:34px;background:#5a5a5a}
.footer h5{font-size:13px;font-weight:600;color:#fff;text-transform:uppercase;letter-spacing:.5px}
.contact{position:absolute;left:360px;top:40px;width:260px}
.contact li{list-style:none;display:flex;gap:12px;margin-top:28px;font-size:10px;line-height:15px}
.contact svg{flex:none;width:16px;height:16px}
.newsletter{position:absolute;left:660px;top:40px;width:220px}
.newsletter .field{margin-top:24px;width:200px;height:28px;background:#fff;border:0}
.newsletter .btn{margin-top:14px;display:inline-block;padding:7px 14px;background:var(--footer-bar);
  color:#fff;font-size:10px;font-weight:700;letter-spacing:.5px}
.menu{position:absolute;left:990px;top:40px;width:120px}
.menu ul{margin-top:20px;list-style:none}
.menu li{font-size:10px;line-height:21px;text-transform:uppercase}
.footer-bar{position:absolute;left:0;top:2160px;width:1200px;height:40px;background:var(--footer-bar);
  color:#9a9a9a;font-size:10px;display:flex;align-items:center;justify-content:center}
.to-top{position:absolute;right:30px;top:2168px;width:26px;height:24px;background:#444;color:#ddd;
  font-size:9px;display:flex;align-items:center;justify-content:center}
</style>
</head>
<body>
<div class="page">

  <header class="hero" role="img" aria-label="Photograph of a detective watching from a car at dusk">
    <div class="hero-shade"></div>
    <div class="brand"><span class="brand-mark"></span>VOSKAMP</div>
    <h1 class="hero-title">VOSKAMP<br>DETECTIVE AGENCY</h1>
    <p class="hero-tag">THE DETECTING WORLD</p>
  </header>

  <nav class="nav">
    <a class="is-active">Home</a>
    <a>About Us</a>
    <a>What We Do</a>
    <a>Our Attorneys<span class="caret">▼</span></a>
    <a>Latest Events<span class="caret">▼</span></a>
    <a>Contact Us</a>
    <a>Testimonials</a>
  </nav>

  <section class="welcome">
    <h2 class="section-title">Welcome to Voskamp Detective Services</h2>
    <p>We uncover the truth for companies, small businesses and private clients with discretion, patience and careful method. Our investigators combine field work, research and modern tools to gather facts that hold up. Every case starts with a confidential talk so we understand what matters to you, and every result is reported clearly, honestly and on time, so you can decide your next step with confidence and peace of mind.</p>
  </section>
  <div class="rule"></div>

  <h2 class="section-title services-title">What We Do</h2>
  <section class="services">
    <div class="service">
      <div class="service-letter">S</div>
      <div><h3>Staff Steeling Data</h3><p>We trace leaks of company data, secure the evidence and name the source so you can act firmly.</p></div>
    </div>
    <div class="service">
      <div class="service-letter">P</div>
      <div><h3>Products</h3><p>Missing stock or goods? We follow the trail from warehouse to buyer with quiet, lawful research.</p></div>
    </div>
    <div class="service">
      <div class="service-letter">D</div>
      <div><h3>Divorce Matters</h3><p>Private cases handled with care: facts on assets, conduct and custody, reported in full confidence.</p></div>
    </div>
  </section>

  <section class="attorneys">
    <h2 class="section-title">Our Attorneys</h2>
    <div class="team">
      <div class="member">
        <div class="member-photo" role="img" aria-label="Portrait photo of James Rowan"></div>
        <h4>James Rowan</h4>
        <p>Senior investigator with years of corporate fraud work and a sharp eye for hidden detail.</p>
        <hr>
      </div>
      <div class="member">
        <div class="member-photo" role="img" aria-label="Portrait photo of John Kerrigan"></div>
        <h4>John Kerrigan</h4>
        <p>Specialist in data theft cases, digital traces and interviews with staff and witnesses.</p>
        <hr>
      </div>
      <div class="member">
        <div class="member-photo" role="img" aria-label="Portrait photo of Richard Mercer"></div>
        <h4>Richard Mercer</h4>
        <p>Handles surveillance and field work across the country, always calm and always discreet.</p>
        <hr>
      </div>
      <div class="member">
        <div class="member-photo" role="img" aria-label="Portrait photo of Patric Joosten"></div>
        <h4>Patric Joosten</h4>
        <p>Advises private clients on family matters and prepares clear reports for legal use.</p>
        <hr>
      </div>
    </div>
  </section>

  <section class="events">
    <h2 class="section-title">Latest Events</h2>
    <div class="event-list">
      <article class="event">
        <div class="event-photo" role="img" aria-label="Photo of a gloved hand at a lock"></div>
        <h4>Lorem Ipsum Dolor Sit</h4>
        <p>A short update on a recent case where patient research brought the missing facts to light.</p>
        <span class="more">READ MORE &gt;&gt;</span>
      </article>
      <article class="event">
        <div class="event-photo" role="img" aria-label="Photo of handcuffed hands"></div>
        <h4>Udu Nemore Latine</h4>
        <p>News from our team about new methods we use to find the truth faster and more safely.</p>
        <span class="more">READ MORE &gt;&gt;</span>
      </article>
      <article class="event">
        <div class="event-photo" role="img" aria-label="Photo of a person in a dim interview room"></div>
        <h4>Cum In Eleifend</h4>
        <p>Insights from a recent seminar on privacy, ethics and the limits of private investigation.</p>
        <span class="more">READ MORE &gt;&gt;</span>
      </article>
    </div>
  </section>

  <footer class="footer">
    <div class="footer-brand"><span class="mark"></span>VOSKAMP</div>
    <div class="contact">
      <h5>Contact Us</h5>
      <ul>
        <li><svg viewBox="0 0 16 16"><path d="M8 1a5 5 0 0 0-5 5c0 4 5 9 5 9s5-5 5-9a5 5 0 0 0-5-5zm0 7a2 2 0 1 1 0-4 2 2 0 0 1 0 4z" fill="#b5b5b5"/></svg><span>Kanaalweg 12, 1234 AB<br>Lindenhaven, Netherlands</span></li>
        <li><svg viewBox="0 0 16 16"><rect x="1" y="3" width="14" height="10" fill="none" stroke="#b5b5b5" stroke-width="1.5"/><path d="M1 3l7 6 7-6" fill="none" stroke="#b5b5b5" stroke-width="1.5"/></svg><span>info@voskamp-agency.example</span></li>
        <li><svg viewBox="0 0 16 16"><path d="M4 1l3 3-2 2c1 2 3 4 5 5l2-2 3 3-2 3C7 15 1 9 1 3z" fill="#b5b5b5"/></svg><span>+31 (0)20 555 0147</span></li>
      </ul>
    </div>
    <div class="newsletter">
      <h5>News Letter</h5>
      <div class="field"></div>
      <span class="btn">SUBSCRIBE</span>
    </div>
    <div class="menu">
      <h5>Main Menus</h5>
      <ul>
        <li>Home</li><li>About Us</li><li>What We Do</li><li>Our Attorneys</li><li>Latest Events</li><li>Contact Us</li>
      </ul>
    </div>
  </footer>
  <div class="footer-bar">All Rights Reserved. Copyright 2015 Voskamp Agency</div>
  <div class="to-top">TOP</div>

</div>
</body>
</html>
```